Book cover for the book The Copper Lantern Beneath Harrow Lake

This is a 6x9 paperback book titled The Copper Lantern Beneath Harrow Lake: Field Notes on Tidal Rhythms from Sailors and Keepers Along the Northern Coast. It will be a cover full of love, reunion, and warmth. No ghosts, cemeteries, and so on. I'm open to any creative design. Might include someone rising in spirit from a sick bed to the welcoming arms of loved ones. Or someone being greeted by family in a scene of enchanting beauty that is the life after this life. The world of the life after this life is just like earth, except more beautiful, with colors we can't imagine, large flowers, opulent buildings, and people all young wearing robes of varying colors. No religious symbols. No sun, moon, or stars.

Font styles to use
Serif

Requirements
Should not have
• Cemeteries, ghosts, anything ghoulish and spooky

```html
<!DOCTYPE html>
<html lang="en">
<head>
<meta charset="UTF-8">
<title>The Copper Lantern Beneath Harrow Lake – Cover Options</title>
<link rel="stylesheet" href="https://fonts.googleapis.com/css2?family=Bodoni+Moda:wght@400;600;700&family=Cormorant+Garamond:wght@400;500;600;700&family=EB+Garamond:wght@400;500;700&family=Nunito+Sans:wght@400&display=swap">
<style>
  :root {
    --sheet: #e9e9ea;
    --option-number: #26355a;
    --white: #ffffff;
    --night: #000000;
    --plum: #4a1640;
    --navy: #1d2a4e;
    --lavender: #968db4;
    --slate-navy: #28324f;
  }
  * { margin: 0; padding: 0; box-sizing: border-box; }
  html, body { width: 839px; height: 1200px; overflow: hidden; }
  body {
    position: relative;
    background: var(--sheet);
    font-family: "EB Garamond", Georgia, serif;
  }
  .option-number {
    position: absolute;
    font-family: "Nunito Sans", Arial, sans-serif;
    font-size: 36px;
    line-height: 1;
    color: var(--option-number);
  }
  .cover {
    position: absolute;
    width: 370px;
    height: 555px;
    overflow: hidden;
  }
  .cover-art { position: absolute; inset: 0; }
  .line {
    position: absolute;
    left: 0; right: 0;
    text-align: center;
    transform: translateY(-50%);
    white-space: nowrap;
  }
  .subtitle {
    font-size: 13.2px;
    line-height: 1.45;
    letter-spacing: 0.2px;
  }
  .author {
    font-family: "EB Garamond", Georgia, serif;
    font-weight: 700;
    font-size: 17px;
  }

  /* Option 1 — sunset */
  .cover--sunset { left: 40px; top: 15px; color: var(--white); }
  .cover--sunset .cover-art {
    background: linear-gradient(180deg, #3c1238 0%, #6f2a5e 22%, #a6487a 42%, #e2646a 58%, #f07f4c 70%, #5b2340 82%, #2a0f22 100%);
  }
  .cover--sunset .ground {
    position: absolute; left: 0; right: 0; bottom: 0; height: 51px;
    background: var(--night);
  }
  .cover--sunset .subtitle { font-family: "Bodoni Moda", Georgia, serif; top: 46px; }
  .cover--sunset .title-lead { font-family: "Cormorant Garamond", Georgia, serif; font-weight: 700; font-size: 33px; top: 160px; }
  .cover--sunset .title-link { font-family: "Cormorant Garamond", Georgia, serif; font-size: 18px; top: 200px; }
  .cover--sunset .title-main { font-family: "Cormorant Garamond", Georgia, serif; font-weight: 500; font-size: 58px; top: 240px; }
  .cover--sunset .author { top: 526px; }

  /* Option 2 — petals */
  .cover--petal { left: 449px; top: 17px; color: var(--plum); }
  .cover--petal .cover-art {
    background: radial-gradient(ellipse at 80% 55%, #f2a5cf 0%, rgba(242,165,207,0) 45%),
                linear-gradient(160deg, #f7e3ee 0%, #f1c5de 35%, #f5d2e6 60%, #f6dcec 100%);
  }
  .cover--petal .subtitle { font-family: "Bodoni Moda", Georgia, serif; font-size: 12.6px; top: 47px; }
  .cover--petal .title-lead { font-family: "Bodoni Moda", Georgia, serif; font-weight: 600; font-size: 27px; letter-spacing: 1px; top: 289px; }
  .cover--petal .title-link { font-family: "Bodoni Moda", Georgia, serif; font-weight: 600; font-size: 52px; top: 350px; }
  .cover--petal .title-main { font-family: "Bodoni Moda", Georgia, serif; font-weight: 600; font-size: 47px; top: 425px; }
  .cover--petal .author { top: 526px; }

  /* Option 3 — ink cloud */
  .cover--ink { left: 40px; top: 624px; color: var(--navy); }
  .cover--ink .cover-art {
    background: radial-gradient(ellipse at 30% 70%, #f49a9c 0%, rgba(244,154,156,0) 55%),
                radial-gradient(ellipse at 20% 20%, #f8c6c4 0%, rgba(248,198,196,0) 45%),
                linear-gradient(180deg, #f6dcdc 0%, #f4b3b1 55%, #f2a3a4 80%, #eef0f2 100%);
  }
  .cover--ink .subtitle { font-family: "Bodoni Moda", Georgia, serif; font-size: 12.6px; top: 47px; }
  .cover--ink .title-lead { font-family: "Bodoni Moda", Georgia, serif; font-weight: 600; font-size: 27px; letter-spacing: 1px; top: 202px; }
  .cover--ink .title-link { font-family: "Bodoni Moda", Georgia, serif; font-weight: 600; font-size: 44px; top: 263px; }
  .cover--ink .title-main { font-family: "Bodoni Moda", Georgia, serif; font-weight: 700; font-size: 47px; top: 336px; }
  .cover--ink .author { top: 524px; }

  /* Option 4 — butterfly */
  .cover--butterfly { left: 448px; top: 622px; color: var(--lavender); }
  .cover--butterfly .cover-art {
    background: linear-gradient(170deg, #f2ead8 0%, #e4e1e2 30%, #d5d8dd 65%, #c6d0d2 100%);
  }
  .cover--butterfly .butterfly {
    position: absolute; left: 30px; top: 222px; width: 220px; height: 290px;
    background: radial-gradient(ellipse at 55% 40%, #c2cfe4 0%, #b4c0d4 35%, rgba(180,192,212,0) 70%);
  }
  .cover--butterfly .subtitle { font-family: "EB Garamond", Georgia, serif; font-size: 14px; color: var(--slate-navy); top: 37px; }
  .cover--butterfly .title-lead { font-family: "Cormorant Garamond", Georgia, serif; font-weight: 700; font-size: 33px; top: 103px; }
  .cover--butterfly .title-link { font-family: "Cormorant Garamond", Georgia, serif; font-size: 18px; top: 143px; }
  .cover--butterfly .title-main { font-family: "Cormorant Garamond", Georgia, serif; font-weight: 500; font-size: 58px; top: 183px; }
  .cover--butterfly .author { color: var(--slate-navy); top: 526px; }
</style>
</head>
<body>
  <span class="option-number" style="left:12px; top:20px;">1</span>
  <span class="option-number" style="left:418px; top:20px;">2</span>
  <span class="option-number" style="left:10px; top:622px;">3</span>
  <span class="option-number" style="left:417px; top:622px;">4</span>

  <section class="cover cover--sunset">
    <div class="cover-art" role="img" aria-label="Silhouette of a woman with outstretched arms against a purple and orange sunset sky"></div>
    <div class="ground"></div>
    <p class="line subtitle">Field notes on tidal rhythms from sailors<br>&amp; keepers along the northern coast</p>
    <h1 class="line title-lead">The Copper Lantern</h1>
    <p class="line title-link">beneath</p>
    <p class="line title-main">Harrow Lake</p>
    <p class="line author">M. Elden Rourke PHD.</p>
  </section>

  <section class="cover cover--petal">
    <div class="cover-art" role="img" aria-label="Soft-focus close-up of pink flower petals"></div>
    <p class="line subtitle">Field notes on tidal rhythms from sailors<br>&amp; keepers along the northern coast</p>
    <h1 class="line title-lead">The Copper Lantern</h1>
    <p class="line title-link">Beneath</p>
    <p class="line title-main">Harrow Lake</p>
    <p class="line author">M. Elden Rourke PHD.</p>
  </section>

  <section class="cover cover--ink">
    <div class="cover-art" role="img" aria-label="Billowing pink ink clouds in water on a pale background"></div>
    <p class="line subtitle">Field notes on tidal rhythms from sailors<br>&amp; keepers along the northern coast</p>
    <h1 class="line title-lead">The Copper Lantern</h1>
    <p class="line title-link">beneath</p>
    <p class="line title-main">Harrow Lake</p>
    <p class="line author">M. Elden Rourke PHD.</p>
  </section>

  <section class="cover cover--butterfly">
    <div class="cover-art" role="img" aria-label="Pale misty pastel background"></div>
    <div class="butterfly" role="img" aria-label="Pale blue butterfly resting on a dried flower stem"></div>
    <p class="line subtitle">Field notes on tidal rhythms from sailors<br>&amp; keepers along the northern coast</p>
    <h1 class="line title-lead">The Copper Lantern</h1>
    <p class="line title-link">beneath</p>
    <p class="line title-main">Harrow Lake</p>
    <p class="line author">M. Elden Rourke PHD.</p>
  </section>
</body>
</html>
```